New Web Design Project

Number of Pages Required

1 page

Requirements
Must have
• An Overview / Background of the Business & Services(not for profit rescue animal farm)
• The Target Market / Audience you are trying to reach (animal lovers)
• Design Specifics; any preferences or ideas for Style, Colour, Imagery, etc (no preferences)

```html
<!DOCTYPE html>
<html lang="en">
<head>
<meta charset="utf-8">
<title>Animal Rescue Farm</title>
<link href="https://fonts.googleapis.com/css2?family=Alegreya+Sans:wght@500;700&family=Lato:wght@400;700&display=swap" rel="stylesheet">
<style>
:root{
  --bg:#eceee9;
  --white:#ffffff;
  --soft:#f7f7f7;
  --ink:#1d1d1f;
  --text:#6d6d72;
  --teal:#3cc39e;
  --violet:#6f6fe0;
  --plum:#9b4fb8;
  --line:#e8e8ea;
}
*{box-sizing:border-box;margin:0;padding:0}
html,body{width:1200px;height:982px;overflow:hidden}
body{background:var(--bg);font-family:"Lato",sans-serif;color:var(--text);position:relative}
h1,h2,h3{font-family:"Alegreya Sans",sans-serif;color:var(--ink);font-weight:700}
.page{position:absolute;top:0;height:982px;background:var(--white);overflow:hidden}
.page-main{left:10px;width:585px}
.page-more{left:605px;width:585px}
.btn{display:inline-block;background:var(--teal);color:#fff;border-radius:20px;font-size:10px;font-weight:700;text-align:center;line-height:26px;height:26px;width:90px}
.btn-outline{background:transparent;border:1.5px solid var(--teal);color:var(--teal);line-height:23px}
.photo{display:block}

/* hero */
.hero{position:relative;height:320px;background:linear-gradient(160deg,#6e73e4 0%,#8a5ccc 55%,#a24fb0 100%);color:#fff}
.hero-photo{position:absolute;inset:0;background:radial-gradient(ellipse at 45% 30%,rgba(255,255,255,.22),transparent 55%),radial-gradient(ellipse at 20% 85%,rgba(255,255,255,.15),transparent 50%)}
.hero-nav{position:absolute;top:17px;right:52px;display:flex;align-items:center;gap:20px}
.menu-icon{width:10px;height:8px;display:block}
.hero-body{position:absolute;left:60px;top:118px;width:250px}
.hero h1{color:#fff;font-size:33px;line-height:1.1;margin-bottom:10px;white-space:nowrap}
.hero p{font-size:7.5px;line-height:1.65;margin-bottom:22px;color:#f2eefc}
.hero .btn{width:80px;height:22px;line-height:22px;font-size:8px}

/* about */
.about{height:218px;display:flex;padding:30px 62px 0 68px;gap:56px}
.about-text{width:180px;padding-top:20px}
.about h2{font-size:19px;margin-bottom:18px}
.about p{font-size:7.5px;line-height:1.65}
.about-photo{width:214px;height:171px;border-radius:3px;background:linear-gradient(180deg,#3f6a2a 0%,#6b9a3c 55%,#8cc24d 75%,#4d3a25 100%)}

/* animals */
.animals{background:var(--soft);height:444px;padding-top:40px;text-align:center;position:relative}
.animals h2{font-size:20px;margin-bottom:24px}
.animal-row{display:flex;justify-content:center;gap:12px}
.animal{width:106px}
.animal .photo{height:124px;margin-bottom:8px}
.animal p{font-size:6.5px;line-height:1.6}
.arrow{position:absolute;top:158px;width:10px;height:20px}
.arrow-left{left:20px}
.arrow-right{right:20px}
.animals .btn{margin-top:30px;width:80px;height:22px;line-height:22px;font-size:7.5px}

/* right page */
.intro{display:grid;grid-template-columns:1fr 1fr;height:300px;border-bottom:1px solid var(--line)}
.intro-copy{padding:30px 40px;font-size:7.5px;line-height:1.7}
.intro-copy-low{padding-top:110px}
.success{padding:38px 60px 0;height:400px}
.success h2{font-size:19px;text-align:center;margin-bottom:30px}
.stories{display:flex;gap:14px;justify-content:center}
.story{width:148px;height:256px;border:1px solid var(--line);box-shadow:0 1px 3px rgba(0,0,0,.05)}
.story .photo{height:104px}
.story-body{padding:18px 12px}
.story h3{font-size:12px;line-height:1.2;font-weight:500;margin-bottom:14px}
.story p{font-size:6.5px;line-height:1.65;margin-bottom:20px;height:40px}
.story .btn{width:82px;height:22px;font-size:7px;line-height:19px}
.support{position:relative;height:282px;background:linear-gradient(160deg,#8b6fdc 0%,#9a57c4 60%,#a54fb2 100%);color:#fff;text-align:center;padding:52px 70px 0}
.support h2{color:#fff;font-size:20px;font-weight:500;margin-bottom:18px}
.support p{font-size:7.5px;line-height:1.7;margin-bottom:24px;color:#f3eefc}
.support .btn{width:80px;height:22px;line-height:22px;font-size:7.5px}
</style>
</head>
<body>

<main class="page page-main">
  <header class="hero">
    <div class="hero-photo" role="img" aria-label="Young calf in a barn under a violet tint"></div>
    <nav class="hero-nav">
      <span class="btn">Donate</span>
      <svg class="menu-icon" viewBox="0 0 10 8"><path d="M0 1h10M0 4h10M0 7h10" stroke="#fff" stroke-width="1"/></svg>
    </nav>
    <div class="hero-body">
      <h1>Animal Rescue Farm</h1>
      <p>Lorem ipsum dolor sit amet, consectetur adipiscing elit, sed do eiusmod tempor incididunt ut labore et dolore magna aliqua. Euismod nisi porta lorem mollis.</p>
      <span class="btn">Donate</span>
    </div>
  </header>

  <section class="about">
    <div class="about-text">
      <h2>About us</h2>
      <p>Lorem ipsum dolor sit amet, consectetur adipiscing elit, sed do eiusmod tempor incididunt ut labore et dolore magna aliqua. Id velit ut tortor pretium viverra suspendisse potenti. Vitae elementum curabitur vitae nunc sed velit dignissim sodales ut. Sed nisi lacus sed viverra tellus in hac habitasse platea. Porttitor leo a diam sollicitudin tempor.</p>
    </div>
    <div class="about-photo photo" role="img" aria-label="Deer grazing in a green forest meadow behind a wooden fence"></div>
  </section>

  <section class="animals">
    <h2>Our animals</h2>
    <svg class="arrow arrow-left" viewBox="0 0 10 20"><path d="M8 2L2 10l6 8" fill="none" stroke="#b8b8bc" stroke-width="1.2"/></svg>
    <div class="animal-row">
      <div class="animal"><div class="photo" role="img" aria-label="Horned cow behind a wooden fence" style="background:linear-gradient(180deg,#5e8fd0,#8a7a63 60%,#6b5a48)"></div><p>It leaves digging through your design asset folders behind and lets you access your icons</p></div>
      <div class="animal"><div class="photo" role="img" aria-label="Piglet resting in straw" style="background:linear-gradient(180deg,#c9a04a,#d99a8a 55%,#b98a3c)"></div><p>Separated they live in Bookmarksgrove right at the coast of the Semantics</p></div>
      <div class="animal"><div class="photo" role="img" aria-label="White lamb in a green field" style="background:linear-gradient(90deg,#e9e3d8,#d8d0c2 60%,#6f9a3a)"></div><p>A small river named Duden flows by their place and supplies it with the necessary regelialia</p></div>
      <div class="animal"><div class="photo" role="img" aria-label="Spotted pig close-up" style="background:linear-gradient(180deg,#7d7468,#c9c2b8 55%,#5d5348)"></div><p>It is a paradisematic country, in which roasted parts of sentences fly into your mouth</p></div>
    </div>
    <svg class="arrow arrow-right" viewBox="0 0 10 20"><path d="M2 2l6 8-6 8" fill="none" stroke="#3cc39e" stroke-width="1.2"/></svg>
    <span class="btn">Donate now</span>
  </section>
</main>

<main class="page page-more">
  <section class="intro">
    <div class="photo" role="img" aria-label="Close-up of a woolly sheep" style="background:linear-gradient(180deg,#cfc8bd,#a89f92 60%,#7a7266)"></div>
    <div class="intro-copy">Lorem ipsum dolor sit amet, consectetur adipiscing elit, sed do eiusmod tempor incididunt ut labore. Vitae nunc sed velit dignissim sodales ut. Sed nisi lacus sed viverra tellus in hac habitasse platea.</div>
    <div class="intro-copy intro-copy-low">Lorem ipsum dolor sit amet, consectetur adipiscing elit, sed do eiusmod tempor incididunt ut labore et dolore magna aliqua. Id velit viverra suspendisse potenti curabitur vitae nunc sed velit sodales. Sed nisi lacus sed viverra tellus.</div>
    <div class="photo" role="img" aria-label="Sow and piglet resting on wood shavings" style="background:linear-gradient(170deg,#d8b26e,#e39a72 45%,#c98a4a 80%,#d9a24c)"></div>
  </section>

  <section class="success">
    <h2>Success stories</h2>
    <div class="stories">
      <article class="story"><div class="photo" role="img" aria-label="Horse in a pasture" style="background:linear-gradient(180deg,#6a9a4a,#8a6a8a)"></div><div class="story-body"><h3>Lorem ipsum dolor sit amet elit</h3><p>Lorem ipsum dolor sit amet, consectetur adipiscing elit sed do.</p><span class="btn btn-outline">Read more</span></div></article>
      <article class="story"><div class="photo" role="img" aria-label="Black and white cow in a grassy field" style="background:linear-gradient(180deg,#5f8f3a,#8a8a80 55%,#6aa03c)"></div><div class="story-body"><h3>Neque laoreet suspendisse interdum</h3><p>Ut labore et dolore magna aliqua. Maecenas accumsan lacus vel facilisis volutpat est velit egestas dui.</p><span class="btn btn-outline">Read more</span></div></article>
      <article class="story"><div class="photo" role="img" aria-label="Girl hugging a brown horse" style="background:linear-gradient(90deg,#8a5a3a,#c89a7a 60%,#d8c04a)"></div><div class="story-body"><h3>Com sociis natoque penatibus et magnis dis</h3><p>Lorem ipsum dolor sit amet, consectetur adipiscing elit, sed do eiusmod tempor incididunt.</p><span class="btn btn-outline">Read more</span></div></article>
    </div>
  </section>

  <section class="support" role="img" aria-label="Horses under a violet tint behind the call to action">
    <h2>Support our cause to save animals</h2>
    <p>Lorem ipsum dolor sit amet, consectetur adipiscing elit, sed do eiusmod tempor incididunt ut labore et dolore magna aliqua. Id velit ut tortor pretium viverra suspendisse potenti. Vitae curabitur vitae nunc sed velit dignissim sodales ut. Sed nisi lacus sed viverra tellus in hac habitasse platea.</p>
    <span class="btn">Sign up</span>
  </section>
</main>

</body>
</html>
```